Wanderlark Gin - Bottle Label for a craft Gin about to be launched on the world from New Zealand

We are a start up craft distillery in New Zealand. We have developed a wonderful Gin using our own grain spirit and both traditional and New Zealand native botanicals (Manuka to be specific), chosen our bottle and the name "Wanderlark" and done a bit of amateur label design and now we are looking for someone to make it great.

Feel free to change up our amateur concept but give us something that will pop from the back bar and scream authenticity, craft and individuality.

The attached files give you the specifications of the bottle, our current concept for a Wanderlark label and an earlier concept drawing that gives an idea of where we are thinking the two labels should go on the front of the bottle.

Thanks, we look forward to your ideas!!

Target Market(s)

High end and craft Gin drinkers. Hipsters and cocktail barflys and their bar tenders and bar owners

Requirements
Must have
• Attractive individuality
Nice to have
• Coolness
Should not have
• Uncoolness

```html
<!DOCTYPE html>
<html lang="en">
<head>
<meta charset="utf-8">
<title>Wanderlark Gin – Bottle Labels</title>
<link href="https://fonts.googleapis.com/css2?family=Didact+Gothic&display=swap" rel="stylesheet">
<style>
  :root {
    --canvas: #ffffff;
    --label-front: #e6f4f7;
    --pattern-soft: #dff0f4;
    --label-back: #cfeaf2;
    --teal: #1fb3c2;
    --teal-light: #7fd3dc;
    --teal-pale: #b5e4ea;
    --purple: #8a4c9f;
    --ink: #222628;
  }
  * { box-sizing: border-box; margin: 0; padding: 0; }
  html, body {
    width: 1200px; height: 1200px; overflow: hidden;
    background: var(--canvas);
    font-family: "Didact Gothic", "Helvetica Neue", Arial, sans-serif;
  }
  .label-set {
    position: absolute;
    left: 352px; top: 298px;
    width: 496px;
  }
  .front-label {
    position: relative;
    margin-top: 40px;
    height: 387px;
    background: var(--label-front);
    text-align: center;
  }
  .label-texture {
    position: absolute; inset: 0;
    background: linear-gradient(160deg, var(--pattern-soft) 0%, var(--label-front) 45%, var(--pattern-soft) 100%);
    z-index: 0;
  }
  .wave-band {
    position: absolute; top: -12px; height: 26px;
    width: 190px;
    background: linear-gradient(180deg, var(--teal-light), var(--teal-pale));
    border-radius: 13px;
    z-index: 1;
  }
  .wave-band.left { left: 0; }
  .wave-band.right { right: 0; }
  .brand-dot {
    position: absolute; left: 50%; top: -38px;
    width: 104px; height: 104px; margin-left: -52px;
    border-radius: 50%;
    background: var(--teal);
    z-index: 2;
  }
  .wordmark {
    position: absolute; left: 0; right: 0; top: 108px;
    font-size: 72px; line-height: 1; letter-spacing: 1px;
    color: var(--purple);
    font-weight: 400;
    z-index: 1;
  }
  .descriptor {
    position: absolute; left: 0; right: 0; top: 236px;
    font-size: 19px; letter-spacing: 1px; color: var(--ink);
    z-index: 1;
  }
  .volume {
    position: absolute; left: 0; right: 0; top: 263px;
    font-size: 11px; letter-spacing: 2px; color: var(--ink);
    z-index: 1;
  }
  .back-label {
    margin-top: 20px;
    height: 155px;
    background: var(--label-back);
    border-radius: 78px;
    position: relative;
    text-align: center;
  }
  .tasting-note {
    padding: 22px 36px 0;
    font-size: 16px; line-height: 1.35;
    color: var(--purple);
  }
  .strength {
    position: absolute; left: 60px; right: 58px; bottom: 10px;
    display: flex; justify-content: space-between;
    font-size: 15px; color: var(--ink);
  }
</style>
</head>
<body>
  <main class="label-set">
    <section class="front-label">
      <div class="label-texture" role="img" aria-label="Soft pale swirl texture across the label"></div>
      <div class="wave-band left" role="img" aria-label="Decorative teal wave ribbon"></div>
      <div class="wave-band right" role="img" aria-label="Decorative teal wave ribbon"></div>
      <div class="brand-dot"></div>
      <h1 class="wordmark">WANDERLARK</h1>
      <p class="descriptor">NEW ZEALAND&nbsp; SMALL&nbsp; BATCH&nbsp; GIN</p>
      <p class="volume">500 ml</p>
    </section>
    <section class="back-label">
      <p class="tasting-note">A classically inspired Gin with a New Zealand twist.&nbsp; Distilled in-house starting with local grain and finished with 11 botanicals including a generous helping of East Coast Manuka cones, Gisborne Citrus and Otago Lavender</p>
      <div class="strength"><span>84 PROOF</span><span>42% ALC. BY VOL.</span></div>
    </section>
  </main>
</body>
</html>
```